Print & Packaging Design for Snug Pip Teething & Healing Necklaces

Bring your Creative Juices this-a way! Smart, savvy, up-market business needs a logo & swing tags! Do you have what it takes?

```html
<!DOCTYPE html>
<html lang="en">
<head>
<meta charset="utf-8">
<title>Snug Pip Swing Tags</title>
<link rel="stylesheet" href="https://fonts.googleapis.com/css2?family=Cabin:wght@400;500&display=swap">
<style>
  :root {
    --backdrop: #b4b4b4;
    --tag-front: #e3ebd4;
    --tag-back: #fdfdfa;
    --ink: #6d6849;
    --cord: #7a7257;
    --rule: #cfcbb8;
    --photo-light: #f0d6c4;
    --photo-dark: #c9a792;
    --beads-light: #8a7a4f;
    --beads-dark: #4f4a33;
  }
  html, body {
    margin: 0;
    padding: 0;
    width: 1200px;
    height: 975px;
    overflow: hidden;
    background: var(--backdrop);
  }
  .sheet {
    position: relative;
    width: 1200px;
    height: 975px;
    font-family: "Cabin", sans-serif;
    color: var(--ink);
  }
  .tags-art { position: absolute; left: 0; top: 0; }
  .text-block {
    position: absolute;
    text-align: center;
    font-weight: 400;
    color: var(--ink);
  }
  .brand-small { left: 420px; top: 262px; width: 160px; font-size: 26px; }
  .brand-large { left: 670px; top: 262px; width: 340px; }
  .brand-large .brand-name { font-size: 64px; line-height: 1; display: block; }
  .brand-large .brand-line { font-size: 17px; display: block; margin-top: 6px; text-align: right; padding-right: 20px; }
  .back-brand { left: 340px; top: 578px; font-size: 34px; }
  .feature-list {
    position: absolute;
    margin: 0;
    padding: 0;
    list-style: none;
    text-align: center;
    font-size: 18px;
    line-height: 1.25;
  }
  .feature-list li { padding: 6px 0; }
  .feature-list.front-list { left: 240px; top: 648px; width: 340px; }
  .feature-list.front-list li + li { border-top: 1px solid var(--rule); }
  .feature-list.back-list { left: 660px; top: 668px; width: 340px; }
  .feature-list.back-list li + li { border-top: 1px solid var(--rule); }
</style>
</head>
<body>
<div class="sheet">
  <svg class="tags-art" width="1200" height="975" viewBox="0 0 1200 975" xmlns="http://www.w3.org/2000/svg">
    <defs>
      <path id="heart" d="M220,70 C220,22 172,0 118,0 C48,0 0,52 0,122 C0,222 128,290 220,348 C312,290 440,222 440,122 C440,52 392,0 322,0 C268,0 220,22 220,70 Z"/>
      <clipPath id="front-left-clip">
        <use href="#heart" transform="translate(187,107)"/>
      </clipPath>
      <linearGradient id="photo-tone" x1="0" y1="0" x2="1" y2="1">
        <stop offset="0" stop-color="var(--photo-light)"/>
        <stop offset="1" stop-color="var(--photo-dark)"/>
      </linearGradient>
      <linearGradient id="bead-tone" x1="0" y1="0" x2="1" y2="0">
        <stop offset="0" stop-color="var(--beads-light)"/>
        <stop offset="1" stop-color="var(--beads-dark)"/>
      </linearGradient>
    </defs>

    <!-- front tag pair -->
    <g class="tag-front">
      <use href="#heart" transform="translate(187,107)" fill="var(--tag-front)"/>
      <use href="#heart" transform="translate(613,107)" fill="var(--tag-front)"/>
      <g role="img" aria-label="Photo of a smiling baby in a striped cap wearing an amber teething necklace">
        <rect x="187" y="107" width="250" height="350" fill="url(#photo-tone)" clip-path="url(#front-left-clip)"/>
      </g>
      <circle cx="475" cy="240" r="12" fill="var(--ink)"/>
      <circle cx="573" cy="224" r="10" fill="var(--backdrop)"/>
      <circle cx="647" cy="224" r="10" fill="var(--backdrop)"/>
      <path d="M573,224 C600,200 640,215 647,224" fill="none" stroke="var(--cord)" stroke-width="4"/>
      <path d="M573,224 C590,270 640,300 605,340 C580,370 640,400 612,430" fill="none" stroke="var(--cord)" stroke-width="4" stroke-linecap="round"/>
      <path d="M647,224 C620,270 570,295 600,335 C625,365 585,395 600,425" fill="none" stroke="var(--cord)" stroke-width="4" stroke-linecap="round"/>
    </g>

    <!-- back tag pair -->
    <g class="tag-back">
      <use href="#heart" transform="translate(187,527)" fill="var(--tag-back)"/>
      <use href="#heart" transform="translate(613,527)" fill="var(--tag-back)"/>
      <circle cx="318" cy="598" r="13" fill="var(--ink)"/>
      <g role="img" aria-label="Illustration of an amber bead teething necklace">
        <rect x="768" y="598" width="160" height="70" rx="30" fill="url(#bead-tone)"/>
      </g>
      <circle cx="587" cy="607" r="10" fill="var(--backdrop)"/>
      <circle cx="653" cy="607" r="10" fill="var(--backdrop)"/>
      <path d="M587,607 C610,585 640,595 653,607" fill="none" stroke="var(--cord)" stroke-width="4"/>
      <path d="M587,607 C600,660 650,690 615,735 C590,765 645,800 620,845" fill="none" stroke="var(--cord)" stroke-width="4" stroke-linecap="round"/>
      <path d="M653,607 C630,660 585,690 610,730 C635,770 595,800 612,850" fill="none" stroke="var(--cord)" stroke-width="4" stroke-linecap="round"/>
    </g>
  </svg>

  <div class="text-block brand-small">Snug Pip</div>
  <div class="text-block brand-large">
    <span class="brand-name">Snug Pip</span>
    <span class="brand-line">Teething &amp; Healing Necklaces</span>
  </div>

  <div class="text-block back-brand">Snug Pip</div>
  <ul class="feature-list front-list">
    <li>Natural pain relief for your babe.</li>
    <li>Baltic amber teething necklaces.</li>
    <li>Gemstone nursing necklaces.</li>
    <li>Relieve your babes pain<br>and sleep better<br>at night.</li>
  </ul>
  <ul class="feature-list back-list">
    <li>Sleep better at night knowing you've<br>helped to ease your babes pain.</li>
    <li>Fertility and birthing jewellery.</li>
    <li>Natural healing jewellery.</li>
  </ul>
</div>
</body>
</html>
```